I need beautiful business cards with Moonpetals and sparrows on then and my tavolink business name is Moonpetals and sparrows.
I sell mini gardens, candles and melts and gift ware....on the other side I would like some thing like...REMEMBER to keep in touch with Moonpetals and sparrows buy a like,comment or just to say hello or tavo link will think you are no longer interested and delete you....you can change the wording to that to make smaller if you would like, and am not sure how to word it....my color theme for my business in purple and green. thank you.

tavo link:Moonpetals and sparrows
mini gardens
candles and melts
gift ware.
email:rosa514@kelvimail.com
phone:0873514062

```html
<!DOCTYPE html>
<html lang="en">
<head>
<meta charset="utf-8">
<title>Moonpetals and Sparrows – Business Cards</title>
<link rel="stylesheet" href="https://fonts.googleapis.com/css2?family=Open+Sans:wght@400;600;800&family=Kalam:wght@400&display=swap">
<style>
  :root {
    --bg: #e9e6e2;
    --card: #ffffff;
    --green: #12984a;
    --green-soft: #8cc49a;
    --purple: #5b2f95;
    --purple-soft: #a58ac8;
    --ink: #111111;
  }
  * { box-sizing: border-box; margin: 0; padding: 0; }
  html, body {
    width: 1200px; height: 1000px; overflow: hidden;
    background: var(--bg);
    font-family: "Open Sans", Arial, sans-serif;
  }
  .canvas { position: relative; width: 1200px; height: 1000px; }

  .card {
    position: absolute;
    background: var(--card);
    box-shadow: 0 6px 18px rgba(0,0,0,.18);
    overflow: hidden;
  }
  .card--front { left: 110px; top: 40px; width: 780px; height: 450px; }
  .card--back  { left: 390px; top: 520px; width: 700px; height: 440px; }

  .art { position: absolute; border-radius: 50%; }
  .art--dragonfly { background: radial-gradient(ellipse at 45% 45%, var(--green) 0%, var(--green-soft) 65%, rgba(140,196,154,0) 72%); }
  .art--butterfly { background: radial-gradient(ellipse at 50% 45%, var(--purple) 0%, var(--purple-soft) 62%, rgba(165,138,200,0) 72%); }

  .brand-name {
    position: absolute; left: 0; right: 0; text-align: center;
    font-family: "Open Sans", Arial, sans-serif; font-weight: 800;
    text-transform: uppercase; color: var(--ink); letter-spacing: .5px;
  }
  .tagline {
    position: absolute; left: 0; right: 0; text-align: center;
    font-family: "Kalam", cursive; color: var(--ink);
  }

  .band { position: absolute; left: 0; right: 0; }

  /* front */
  .card--front .brand-name { top: 290px; font-size: 40px; }
  .card--front .tagline { top: 340px; font-size: 30px; }
  .card--front .band--thin { bottom: 66px; height: 7px; background: var(--purple); }
  .card--front .band--thick { bottom: 0; height: 56px; background: var(--green); }

  /* back */
  .card--back .brand-name { top: 120px; font-size: 24px; }
  .card--back .tagline { top: 150px; font-size: 16px; }
  .contact {
    position: absolute; left: 40px; right: 40px; top: 200px;
    text-align: center; font-size: 18px; line-height: 26px; color: var(--green);
  }
  .contact .label { color: var(--purple); }
  .note {
    position: absolute; left: 20px; right: 20px; top: 330px;
    text-align: center; font-size: 12.5px; line-height: 19px; color: var(--ink);
  }
  .card--back .band--thin { bottom: 40px; height: 5px; background: var(--green); }
  .card--back .band--thick { bottom: 0; height: 32px; background: var(--purple); }
</style>
</head>
<body>
<main class="canvas">

  <section class="card card--front" aria-label="Business card front">
    <div class="art art--dragonfly" role="img" aria-label="Green dragonfly illustration" style="left:120px;top:70px;width:280px;height:220px;"></div>
    <div class="art art--dragonfly" role="img" aria-label="Small green dragonfly illustration" style="left:430px;top:225px;width:50px;height:40px;"></div>
    <div class="art art--butterfly" role="img" aria-label="Purple swirling butterfly illustration" style="left:400px;top:20px;width:300px;height:230px;"></div>
    <div class="art art--butterfly" role="img" aria-label="Small purple butterfly illustration" style="left:300px;top:60px;width:44px;height:36px;"></div>

    <h1 class="brand-name">Moonpetals and Sparrows</h1>
    <p class="tagline">Mini Gardens, Candles and Melts Gift Ware</p>

    <div class="band band--thin"></div>
    <div class="band band--thick"></div>
  </section>

  <section class="card card--back" aria-label="Business card back">
    <div class="art art--dragonfly" role="img" aria-label="Green dragonfly illustration" style="left:235px;top:10px;width:140px;height:100px;"></div>
    <div class="art art--butterfly" role="img" aria-label="Purple swirling butterfly illustration" style="left:340px;top:0;width:150px;height:110px;"></div>

    <h2 class="brand-name">Moonpetals and Sparrows</h2>
    <p class="tagline">Mini Gardens, Candles and Melts Gift Ware</p>

    <div class="contact">
      <p><span class="label">Email:</span>rosa514@kelvimail.com</p>
      <p><span class="label">Phone:</span>0873514062</p>
      <p><span class="label">Tavolink:</span>Moonpetals and sparrows mini gardens, candles<br>and melts gift ware.</p>
    </div>

    <p class="note">Don't forget to keep in touch with Moonpetals and sparrows.<br>Like and Comment us otherwise Tavolink will think that you are not interested and delete you.</p>

    <div class="band band--thin"></div>
    <div class="band band--thick"></div>
  </section>

</main>
</body>
</html>
```